Webdesign for a Bikeshop in Innsbruck (male audience)

To obtain my master's degree, I am conducting a study in the field of web design as part of my master thesis. All submitted designs will therefore be used for study purposes. In order to achieve a homogeneous group, I would like to encourage not only male but also female web designers to submit a design. All submitted designs will be used anonymously for the study and therefore do not allow any conclusions to be drawn about your person. Since this is a contest, the winner will be chosen randomly from all serious submissions. I would be really happy if you would support me in my study. I think the results could be very informative and also useful for your further work (I won't go into more detail here as it could skew the results - but once the contest is over, feel free to contact me. Of course I will also provide you with my results as soon as my work is finished). Below you will find a fictitious usecase and a description of what the website should include:

The company Brenvik Outfitters is planning to relaunch its own website and would like to present itself primarily as a competent and leading consultant in the field of cargo bikes. The design should appeal to a broad audience and embody an urban lifestyle. In any case, the website should include a landing page, a product overview page and a product details page. The company also wants to appeal mainly to a MALE target group. You only design the website. So don't worry about hardware or software limitations, just create the best bike store design you can.

As it is fictitious, I can't offer any materials. A logo is not necessary, you can use a placeholder or whatever you have access to. If you need any inspring websites feel free to contact me.

Target Market(s)

male users

Number of Pages Required

1 page

Requirements
Must have
• landing page, product overview page, product details page
Should not have
• online shop

```html
<!DOCTYPE html>
<html lang="en">
<head>
<meta charset="utf-8">
<title>Brenvik Outfitters – Cargo Bikes</title>
<link href="https://fonts.googleapis.com/css2?family=Montserrat:ital,wght@0,400;0,500;0,600;0,700;1,500&family=Open+Sans:wght@400;600&display=swap" rel="stylesheet">
<style>
:root{
  --orange:#ef6239;
  --ink:#1d1d1d;
  --text:#333333;
  --muted:#6b6b6b;
  --light-bg:#f5f5f5;
  --footer-bg:#1c1c1c;
  --line:#bdbdbd;
  --white:#ffffff;
}
*{margin:0;padding:0;box-sizing:border-box}
html,body{width:1200px;height:3883px;overflow:hidden}
body{font-family:'Montserrat',sans-serif;color:var(--text);background:var(--white);position:relative}
.abs{position:absolute}
a{color:inherit;text-decoration:none}

/* header */
.site-header{position:absolute;left:0;top:0;width:1200px;height:104px;background:var(--white)}
.brand-name{font-weight:700;font-size:21px;color:var(--ink);letter-spacing:.2px;text-transform:uppercase}
.brand-tag{font-family:'Open Sans',sans-serif;font-size:18px;color:var(--muted)}
.site-header .brand-name{left:110px;top:28px}
.site-header .brand-tag{left:112px;top:56px}
.main-nav a{position:absolute;top:40px;font-size:17px;font-weight:500;color:var(--ink)}
.main-nav a.active{color:var(--orange)}
.call{display:flex;align-items:center;gap:10px;font-weight:600;font-size:17px;color:var(--ink)}
.call-ring{width:36px;height:36px;border:1.5px solid var(--line);border-radius:50%;display:flex;align-items:center;justify-content:center}

/* hero */
.hero{left:0;top:104px;width:1200px;height:651px;border-bottom-right-radius:170px;overflow:hidden;
  background:linear-gradient(100deg,#4e4a33 0%,#6b5a3a 35%,#8a6a44 55%,#5d5b4c 80%,#7d7a6d 100%)}
.hero-photo{position:absolute;inset:0}
.hero h1{position:absolute;left:111px;top:150px;font-size:50px;line-height:62px;font-weight:700;color:var(--white);text-transform:uppercase}
.hero p{position:absolute;left:111px;top:288px;width:460px;font-family:'Open Sans',sans-serif;font-size:20px;line-height:37px;color:var(--white)}
.btn{display:flex;align-items:center;justify-content:center;background:var(--orange);color:var(--white);border-radius:40px;text-transform:uppercase}
.hero .btn{position:absolute;left:111px;top:395px;width:360px;height:69px;font-family:'Open Sans',sans-serif;font-size:18px;font-weight:600}

/* welcome */
.section-title{position:absolute;left:0;width:1200px;text-align:center;font-size:36px;font-weight:700;color:var(--ink);text-transform:uppercase}
.welcome-text{left:170px;top:886px;width:860px;text-align:center;font-size:16px;line-height:26.5px;color:var(--muted)}
.video-btn{left:466px;top:998px;width:268px;height:57px;font-size:17px;font-weight:600;gap:14px;justify-content:flex-start;padding-left:10px}
.play{width:40px;height:40px;border-radius:50%;background:var(--white);display:flex;align-items:center;justify-content:center}
.bike-feature{left:68px;top:1075px;width:1040px;height:440px;border-radius:28px 28px 0 0;
  background:linear-gradient(180deg,#fbf7f4 0%,#f6ece4 45%,#efe3da 75%,#f5f5f5 100%)}

/* products */
.products{left:0;top:1515px;width:1200px;height:638px;background:var(--light-bg)}
.product-card{position:absolute;top:137px;width:466px}
.product-photo{width:466px;height:385px;border-bottom-right-radius:62px}
.product-card h3{margin-top:17px;text-align:center;font-size:26px;font-weight:500;color:var(--text)}

/* features */
.feature{position:absolute;top:2297px;width:256px;text-align:center}
.feature-ring{width:154px;height:154px;margin:0 auto;border:1.5px solid #9a9a9a;border-radius:50%;display:flex;align-items:center;justify-content:center}
.feature h4{margin-top:20px;font-size:22px;font-weight:500;color:var(--text);letter-spacing:.3px}

/* testimonials */
.testimonials{left:0;top:2558px;width:1200px;height:455px;border-top-left-radius:115px;border-bottom-right-radius:115px;
  background:linear-gradient(120deg,#ee6a3e 0%,#f07245 40%,#e8643a 70%,#ec6c40 100%)}
.testimonials h2{position:absolute;left:0;width:1200px;top:59px;text-align:center;font-size:36px;font-weight:700;color:var(--white);text-transform:uppercase}
.testimonials blockquote{position:absolute;left:170px;top:135px;width:860px;text-align:center;font-style:italic;font-weight:500;font-size:22px;line-height:33.5px;color:var(--white)}
.testimonials cite{position:absolute;left:0;width:1200px;top:305px;text-align:center;font-style:normal;font-size:18px;color:var(--white)}
.dots{position:absolute;top:378px;left:583px;display:flex;gap:3px}
.dots span{width:9px;height:9px;border-radius:50%;background:var(--white)}
.dots span.on{background:#f7b733}

/* journey */
.journey h2{position:absolute;left:111px;top:3115px;font-size:36px;line-height:48px;font-weight:700;color:var(--ink);text-transform:uppercase}
.journey p{position:absolute;left:111px;top:3237px;width:460px;font-size:16px;line-height:26.5px;color:var(--muted)}
.journey-photo{left:613px;top:3089px;width:475px;height:363px;border-bottom-left-radius:62px;
  background:linear-gradient(90deg,#e4e6e8 0%,#cfd3d6 40%,#8c96a6 60%,#d8dadc 100%)}

/* footer */
.site-footer{left:0;top:3520px;width:1200px;height:363px;background:var(--footer-bg);border-top-left-radius:115px;color:var(--white)}
.site-footer .brand-name{position:absolute;left:110px;top:87px;font-size:28px;color:var(--white)}
.site-footer .brand-tag{position:absolute;left:112px;top:125px;font-size:22px;color:var(--white)}
.site-footer .call{position:absolute;left:111px;top:178px;color:var(--white)}
.site-footer .call-ring{border-color:#666}
.foot-col{position:absolute;top:84px}
.foot-col h5{font-size:20px;font-weight:500;margin-bottom:14px}
.foot-col a{display:block;font-size:16px;line-height:28px;color:#e6e6e6}
.foot-rule{left:111px;top:267px;width:977px;height:1px;background:#444}
.copyright{left:111px;top:302px;font-size:16px;color:#e6e6e6}
.social{position:absolute;top:292px;width:42px;height:42px;border:1.5px solid var(--orange);border-radius:50%;display:flex;align-items:center;justify-content:center}
</style>
</head>
<body>

<header class="site-header">
  <div class="abs brand-name">Brenvik Outfitters</div>
  <div class="abs brand-tag">Cargo Bikes</div>
  <nav class="main-nav">
    <a class="active" href="#" style="left:418px">Home</a>
    <a href="#" style="left:503px">About</a>
    <a href="#" style="left:591px">Products</a>
    <a href="#" style="left:704px">Contact</a>
  </nav>
  <div class="abs call" style="left:876px;top:32px">
    <span class="call-ring"><svg width="16" height="16" viewBox="0 0 24 24"><path fill="var(--orange)" d="M6.6 10.8a15.1 15.1 0 0 0 6.6 6.6l2.2-2.2c.3-.3.7-.4 1-.2 1.1.4 2.300.6 3.6.6.6 0 1 .4 1 1V20c0 .6-.4 1-1 1C10.6 21 3 13.4 3 4c0-.6.4-1 1-1h3.5c.6 0 1 .4 1 1 0 1.3.2 2.5.6 3.6.1.3 0 .7-.2 1z"/></svg></span>
    Call: 188 555 0142
  </div>
</header>

<section class="abs hero">
  <div class="hero-photo" role="img" aria-label="Photo of a smiling couple riding a wooden cargo bike with a child in the front box on a city street"></div>
  <h1>Urban Lifestlye<br>Cargo Bikes</h1>
  <p>Duis aute irure dolor in reprehenderit in volup tate velit esse cillum dolore..</p>
  <a class="btn" href="#">Schedule a free test ride now</a>
</section>

<h2 class="section-title" style="top:818px">Welcome to Brenvik Outfitters</h2>
<p class="abs welcome-text">Lorem ipsum dolor sit amet, consectetur adipiscing elit, sed do eiusmod tempor incididunt ut labore et dolore magna aliqua. Ut enim ad minim veniam quis nostrud exercitation ullamco laboris nisi ut aliquip ex ea commodo consequa ute irure dolor in reprehend erit in voluptate velit esse cillu.</p>
<a class="abs btn video-btn" href="#"><span class="play"><svg width="16" height="18" viewBox="0 0 16 18"><path d="M2 1l13 8-13 8z" fill="var(--ink)"/></svg></span>Watch our video</a>
<div class="abs bike-feature" role="img" aria-label="Cutout photo of an orange wooden-box cargo bike with dark green frame, shown from the side"></div>

<section class="abs products">
  <h2 class="section-title" style="top:55px">Products</h2>
  <div class="product-card" style="left:111px">
    <div class="product-photo" role="img" aria-label="Photo of a father riding a family cargo bike with children on a town square" style="background:linear-gradient(160deg,#a4826a 0%,#8a7060 40%,#b8aa9a 70%,#7a6c62 100%)"></div>
    <h3>Persons</h3>
  </div>
  <div class="product-card" style="left:623px">
    <div class="product-photo" role="img" aria-label="Photo of a courier riding a delivery cargo bike with an orange cargo box on a city road" style="background:linear-gradient(160deg,#8f9aa0 0%,#767b7d 45%,#8a7f78 75%,#9a8f88 100%)"></div>
    <h3>Transport loads</h3>
  </div>
</section>

<h2 class="section-title" style="top:2215px">Why choose Brenvik Outfitters</h2>
<div class="feature" style="left:100px">
  <div class="feature-ring"><svg width="80" height="60" viewBox="0 0 80 60" fill="none" stroke="var(--orange)" stroke-width="2"><circle cx="14" cy="42" r="11"/><circle cx="64" cy="42" r="11"/><path d="M14 42l12-18h14l-8 18zM26 24l-3-8h-6M40 24l6-12h6M44 26h30v14"/></svg></div>
  <h4>High load capacity</h4>
</div>
<div class="feature" style="left:356px">
  <div class="feature-ring"><svg width="70" height="80" viewBox="0 0 70 80" fill="none" stroke="var(--orange)" stroke-width="2"><circle cx="22" cy="10" r="6"/><path d="M12 26h20v16H12zM20 42v30"/><path d="M34 36l22-8 10 4v18c0 12-10 20-22 24-8-3-12-8-12-8z"/><path d="M38 52l8 8 14-16"/></svg></div>
  <h4>Safety</h4>
</div>
<div class="feature" style="left:611px">
  <div class="feature-ring"><svg width="76" height="76" viewBox="0 0 76 76" fill="none" stroke="var(--orange)" stroke-width="2"><circle cx="38" cy="38" r="24"/><path d="M20 26c8 2 10 8 6 14s4 10 8 18M46 16c-2 8 6 10 14 10M50 40c-6 2-6 10 0 16"/><path d="M8 38a30 30 0 0 1 30-30M68 38a30 30 0 0 1-30 30"/></svg></div>
  <h4>Eco-friendliness</h4>
</div>
<div class="feature" style="left:867px">
  <div class="feature-ring"><svg width="80" height="80" viewBox="0 0 80 80" fill="none" stroke="var(--orange)" stroke-width="2"><circle cx="40" cy="40" r="8"/><circle cx="40" cy="40" r="15" stroke-dasharray="6 4"/><path d="M16 30a26 26 0 0 1 40-16l-2-7M64 50a26 26 0 0 1-40 16l2 7M56 14l-8 1M24 66l8-1"/></svg></div>
  <h4>Sustainability</h4>
</div>

<section class="abs testimonials" aria-label="Client testimonials">
  <h2>Client testimonials</h2>
  <blockquote>“ Nemo enim ipsam voluptatem quia voluptas sit aspernatur aut odit aut fugit, sed quia consequuntur magni dolores eos qui ratione voluptatem se qui nesciunt. Neque porro quisquam est, qui dolorem ipsum quia dolor sit amet, consectetur, numquam eius modi tempora incid.”</blockquote>
  <cite>—Tobias Renner, Procurement Manager</cite>
  <div class="dots"><span></span><span class="on"></span><span></span></div>
</section>

<section class="journey">
  <h2>Journey over<br>destination</h2>
  <p>Lorem ipsum dolor sit amet, consectetur adipiscing elit, sed do eiusmod tempor incididunt ut labore et dolore magna aliqua. Ut enim ad minim veniam quis nostrud exercitation ullamco laboris nisi ut aliquip ex ea comm odo consequa ute irure dolor in repr labore et dolore magna aliqua. Ut enim ad minim.</p>
  <div class="abs journey-photo" role="img" aria-label="Photo of a man in a blue shirt riding a black and white cargo bike past a white van"></div>
</section>

<footer class="abs site-footer">
  <div class="brand-name">Brenvik Outfitters</div>
  <div class="brand-tag">Cargo Bikes</div>
  <div class="call">
    <span class="call-ring"><svg width="16" height="16" viewBox="0 0 24 24"><path fill="var(--orange)" d="M6.6 10.8a15.1 15.1 0 0 0 6.6 6.6l2.2-2.2c.3-.3.7-.4 1-.2 1.1.4 2.3.6 3.6.6.6 0 1 .4 1 1V20c0 .6-.4 1-1 1C10.6 21 3 13.4 3 4c0-.6.4-1 1-1h3.5c.6 0 1 .4 1 1 0 1.3.2 2.5.6 3.6.1.3 0 .7-.2 1z"/></svg></span>
    Call: 188 555 0142
  </div>
  <div class="foot-col" style="left:493px"><h5>Quick Links</h5><a href="#">Home</a><a href="#">About</a><a href="#">Products</a><a href="#">Contact</a></div>
  <div class="foot-col" style="left:682px"><h5>Products</h5><a href="#">Family Bikes</a><a href="#">Business Bikes</a></div>
  <div class="foot-col" style="left:879px"><h5>Information</h5><a href="#">Terms and conditions</a><a href="#">Privacy Policy</a></div>
  <div class="abs foot-rule"></div>
  <div class="abs copyright">2022 © Copyright, Brenvik Outfitters. All rights reserved.</div>
  <a class="social" href="#" aria-label="Social profile" style="left:944px"><svg width="16" height="16" viewBox="0 0 16 16" fill="none" stroke="var(--orange)" stroke-width="1.8" stroke-linecap="round"><path d="M4 12L12 4M6 4h6v6"/></svg></a>
  <a class="social" href="#" aria-label="Social profile" style="left:995px"><svg width="16" height="16" viewBox="0 0 16 16" fill="none" stroke="var(--orange)" stroke-width="1.8" stroke-linecap="round"><path d="M4 12L12 4M6 4h6v6"/></svg></a>
  <a class="social" href="#" aria-label="Social profile" style="left:1046px"><svg width="16" height="16" viewBox="0 0 16 16" fill="none" stroke="var(--orange)" stroke-width="1.8" stroke-linecap="round"><path d="M4 12L12 4M6 4h6v6"/></svg></a>
</footer>

</body>
</html>
```